Pemberly Senior Marketing Biz Card
Biz card and Stationary
Bright & Fun-filled
Marlene Pemberly
Independent Agent
Cedar Vale, OH
marlenej.pemberly@postvale-mail.com
PemberlyForSeniors.com
please add photo headshot to the front of the card also. see upload.
Also, please only use white and blue for the wording on the card. DO NOT USE RED.
see upload example for content for back of card
Logo- please use
Headshot
card back content

```html
<!DOCTYPE html>
<html lang="en">
<head>
<meta charset="utf-8">
<title>Pemberly Senior Marketing – Business Card</title>
<link href="https://fonts.googleapis.com/css2?family=Cinzel:wght@400;600&family=Tinos:ital,wght@0,400;0,700;1,400&family=Arimo:wght@400;700&display=swap" rel="stylesheet">
<style>
  :root {
    --stage: #6b6b6b;
    --navy: #0d3a7a;
    --blue: #1456a8;
    --blue-light: #2b74c9;
    --ink: #1c2f5c;
    --text-dark: #333a44;
    --white: #ffffff;
    --accent-red: #c4222f;
    --pale: #e6edf5;
  }
  * { box-sizing: border-box; margin: 0; padding: 0; }
  html, body { width: 1200px; height: 901px; overflow: hidden; }
  body { background: var(--stage); position: relative; font-family: "Tinos", serif; }

  .card {
    position: absolute;
    width: 700px;
    height: 400px;
    left: 250px;
    overflow: hidden;
    box-shadow: 0 10px 28px rgba(0,0,0,.35);
  }

  /* ---------- back of card ---------- */
  .card-back {
    top: 30px;
    background: radial-gradient(ellipse at 70% 30%, var(--blue-light) 0%, var(--blue) 45%, var(--navy) 100%);
    color: var(--white);
  }
  .card-back .emblem-area {
    position: absolute;
    left: -40px; top: 60px;
    width: 150px; height: 320px;
    border-radius: 50%;
    background: radial-gradient(ellipse, rgba(255,255,255,.16), rgba(255,255,255,0) 70%);
  }
  .brand-name {
    position: absolute;
    font-family: "Tinos", serif;
    font-weight: 700;
    white-space: nowrap;
    line-height: 1;
  }
  .card-back .brand-name {
    right: 36px; top: 40px;
    color: var(--white); font-size: 22px;
  }
  .services {
    position: absolute; left: 80px; top: 140px;
    font-family: "Arimo", sans-serif;
  }
  .services h2 { font-size: 25px; font-weight: 700; margin-bottom: 10px; }
  .services ul { list-style: none; }
  .services li {
    font-size: 20px; line-height: 28px;
    display: flex; align-items: center; gap: 12px;
  }
  .services li::before {
    content: ""; width: 9px; height: 9px; background: var(--accent-red); flex: none;
  }

  /* ---------- front of card ---------- */
  .card-front {
    top: 470px;
    background: var(--white);
  }
  .card-front .emblem-area {
    position: absolute; right: -30px; top: 30px;
    width: 220px; height: 300px; border-radius: 50%;
    background: radial-gradient(ellipse, var(--pale), rgba(230,237,245,0) 70%);
  }
  .card-front .brand-name {
    left: 60px; top: 46px;
    color: var(--blue); font-size: 38px;
  }
  .agent { position: absolute; left: 60px; top: 128px; color: var(--ink); }
  .agent-name { font-size: 24px; font-weight: 700; }
  .agent-title { font-size: 18px; color: var(--text-dark); margin-top: 2px; }
  .contact { list-style: none; margin-top: 14px; }
  .contact li {
    display: flex; align-items: center; gap: 10px;
    font-size: 17px; line-height: 25px; color: var(--text-dark);
  }
  .contact svg { width: 16px; height: 16px; flex: none; }
  .headshot {
    position: absolute; right: 66px; top: 150px;
    width: 150px; height: 176px;
    border: 4px solid var(--blue); border-radius: 10px;
    background: linear-gradient(160deg, #d9dde2, #8c8f95 60%, #3a3a3f);
  }
  .tagline-band {
    position: absolute; left: 0; bottom: 0;
    width: 100%; height: 46px;
    background: linear-gradient(90deg, var(--navy), var(--blue), var(--navy));
    border-top: 4px solid var(--accent-red);
    display: flex; align-items: center; justify-content: center;
    font-family: "Cinzel", serif; font-size: 17px; letter-spacing: .5px;
    color: var(--white);
  }
</style>
</head>
<body>

  <section class="card card-back" aria-label="Business card back">
    <div class="emblem-area" role="img" aria-label="Faint medical staff emblem decoration"></div>
    <div class="brand-name">Pemberly Senior Marketing</div>
    <div class="services">
      <h2>I can also help you with......</h2>
      <ul>
        <li>Long-Term Care Insurance</li>
        <li>Fixed Annuities</li>
        <li>Life Insurance</li>
        <li>Medicare Supplement Insurance</li>
        <li>Individual Major Medical Insurance</li>
        <li>Final Expense Insurance</li>
        <li>Medicare Advantage Plans</li>
      </ul>
    </div>
  </section>

  <section class="card card-front" aria-label="Business card front">
    <div class="emblem-area" role="img" aria-label="Faint medical staff emblem decoration"></div>
    <div class="brand-name">Pemberly Senior Marketing</div>

    <div class="agent">
      <div class="agent-name">Marlene Pemberly</div>
      <div class="agent-title">Independent Agent</div>
      <ul class="contact">
        <li>
          <svg viewBox="0 0 16 16"><path d="M8 1a5 5 0 0 0-5 5c0 4 5 9 5 9s5-5 5-9a5 5 0 0 0-5-5zm0 7a2 2 0 1 1 0-4 2 2 0 0 1 0 4z" fill="#1456a8"/></svg>
          Cedar Vale, OH
        </li>
        <li>
          <svg viewBox="0 0 16 16"><path d="M4 1l3 3-2 2c1 2 3 4 5 5l2-2 3 3-2 3C7 15 1 9 1 3z" fill="#1456a8"/></svg>
          614.555-0142
        </li>
        <li>
          <svg viewBox="0 0 16 16"><rect x="4" y="1" width="8" height="14" rx="1.5" fill="#1456a8"/><rect x="5.5" y="3" width="5" height="8" fill="#fff"/></svg>
          614.555-0187
        </li>
        <li>
          <svg viewBox="0 0 16 16"><rect x="1" y="3" width="14" height="10" rx="1" fill="#1456a8"/><path d="M1.5 4l6.5 5 6.5-5" stroke="#fff" stroke-width="1.3" fill="none"/></svg>
          marlenej.pemberly@postvale-mail.com
        </li>
        <li>
          <svg viewBox="0 0 16 16"><circle cx="8" cy="8" r="6.5" fill="none" stroke="#1456a8" stroke-width="1.5"/><path d="M1.5 8h13M8 1.5c-3 3-3 10 0 13M8 1.5c3 3 3 10 0 13" stroke="#1456a8" stroke-width="1.2" fill="none"/></svg>
          www.PemberlyForSeniors.com
        </li>
      </ul>
    </div>

    <div class="headshot" role="img" aria-label="Headshot photo of Marlene Pemberly"></div>

    <div class="tagline-band">"The One to Call for All of Your Insurance Needs"</div>
  </section>

</body>
</html>
```